Corporate Branded Documents - IT Provider - On-going work

Hi, I'm Neil a Director of Harbourline Tech Care a UK Based IT & Telecoms support firm. We've been trading for 12 years now and feel its time for a lick of paint. We have a logo, website etc but would like someone to create some standard documents for us.

- A PDF Proposal Template - We currently don't send our customers proposals as we have nothing that looks good.
- A Quote Template PDF - Example Attached
- A Order Template PDF - Example Attached
- A Invoice Template PDF - Example Attached
- A Generic Document PDF - Something we can use for customer application forms, NDA Agreements, Terms & Conditions etc

Our website can be found at www.harbourlinetechcare.co.uk - here you'll get a feel for our branding. I've also attached 2 example documents - as well as our currently used documents. Hopefully you guys can see why it needs improving.

We'd also like to work with someone long term, these documents are a start but we'd like to make sure all the work we do looks and feels as smart as possible, so there is plenty of additional work available.

None of these templates need to be Print ready, 99% of the time it will be viewed digitally, so high resolution designs are best

Thanks,

Neil

Target Market(s)

Corporate & Educational Customers

Industry/Entity Type

It Support

Font styles to use
Sans Serif

Colors
ec1f27
0692cd
ffffff

```html
<!DOCTYPE html>
<html lang="en">
<head>
<meta charset="UTF-8">
<title>Harbourline Tech Care – Generic Document</title>
<link href="https://fonts.googleapis.com/css2?family=Carlito:wght@400;700&display=swap" rel="stylesheet">
<style>
  :root {
    --brand-teal: #0f7c91;
    --heading-grey: #555658;
    --body-grey: #6a6a6a;
    --footer-red: #d8313a;
    --paper: #ffffff;
  }
  * { margin: 0; padding: 0; box-sizing: border-box; }
  html, body { width: 851px; height: 1200px; overflow: hidden; background: var(--paper); }
  body { font-family: "Carlito", "Calibri", Arial, sans-serif; }
  .page { position: relative; width: 851px; height: 1200px; background: var(--paper); }

  .masthead {
    position: absolute; left: 0; top: 0; width: 851px; height: 76px;
    background: var(--brand-teal);
  }
  .brand {
    position: absolute; right: 30px; top: 20px;
    display: flex; align-items: center; gap: 10px;
    color: var(--paper); font-weight: 700; font-size: 24px; line-height: 1;
  }
  .brand-mark { width: 20px; height: 20px; background: var(--paper); }

  .title {
    position: absolute; left: 41px; top: 146px; width: 770px;
    color: var(--brand-teal); font-weight: 700; font-size: 24px; line-height: 36px;
  }
  .subtitle-main {
    position: absolute; left: 41px; top: 239px; width: 770px;
    color: var(--heading-grey); font-weight: 700; font-size: 24px; line-height: 35px;
  }
  .intro {
    position: absolute; left: 41px; top: 337px; width: 770px;
    color: var(--body-grey); font-size: 19.5px; line-height: 32.5px;
  }

  .column {
    position: absolute; top: 505px; width: 344px;
    color: var(--body-grey); font-size: 18px; line-height: 31.4px;
    text-align: justify;
  }
  .column-left { left: 46px; }
  .column-right { left: 461px; top: 504px; }
  .column h3 {
    color: var(--brand-teal); font-weight: 700; font-size: 22px; line-height: 33px;
    text-align: left;
  }

  .footer {
    position: absolute; left: 0; bottom: 0; width: 851px; height: 37px;
    background: var(--footer-red); color: var(--paper);
    display: flex; align-items: center; justify-content: space-between;
    padding: 0 20px 0 10px; font-size: 18px;
  }
  .page-number { font-weight: 700; font-size: 20px; }
</style>
</head>
<body>
<div class="page">
  <header class="masthead">
    <div class="brand"><span class="brand-mark"></span>Harbourline Tech Care</div>
  </header>

  <h1 class="title">Lorem Ipsum is simply dummy text of the printing and typesetting industry typesetting industry</h1>
  <h2 class="subtitle-main">Lorem Ipsum is simply dummy text of the printing and typesetting industry typesetting industry</h2>

  <p class="intro">Lorem Ipsum is simply dummy text of the printing and typesetting industry. Lorem Ipsum has been the industry's industry. Lorem Ipsum has been the finishLorem Ipsum is simply dummy text of the printing and typesetting industry. Lorem Ipsum has been the industry's industry. Lorem Ipsum has been the finish</p>

  <section class="column column-left">
    <h3>Subtitle Here</h3>
    <p>Lorem Ipsum is simply dummy text of the printing and typesetting industry. Lorem Ipsum has been the industry's industry. Lorem Ipsum has been the finishLorem Ipsum is simply dummy text of the printing and typesetting industry. Lorem Ipsum has been the industry's industry. Lorem Ipsum has been the finishLorem Ipsum is simply dummy text of the printing and typesetting industry. Lorem Ipsum has been the industry's industry. Lorem Ipsum has been the finishLorem Ipsum is simply dummy text of the printing and typesetting industry. Lorem Ipsum has been the industry's industry. Lorem Ipsum has been the finish.</p>
  </section>

  <section class="column column-right">
    <p>Lorem Ipsum is simply dummy text of the printing and typesetting industry. Lorem Ipsum has been the industry's industry.</p>
    <p>Lorem Ipsum has been the finishLorem Ipsum is simply dummy text of the printing and typesetting industry. Lorem Ipsum has been the industry's industry. Lorem Ipsum has been the finishLorem Ipsum is simply dummy text of the printing and typesetting industry. Lorem Ipsum has been the industry's industry. Lorem Ipsum has been the finishLorem Ipsum is simply dummy text of the printing and typesetting industry.Lorem Ipsum has been the industry's industry. Lorem Ipsum has been the finish.</p>
  </section>

  <footer class="footer">
    <span class="copyright">Copright text here</span>
    <span class="page-number">1</span>
  </footer>
</div>
</body>
</html>
```